Book Cover "Venice"

Creation of a cover (14 x 20.5 cm + bleed area) for a book:
Image: “BrumeVerte” (Tiff joined)
AUTHOR: Maribel Quonte
TITLE: The murmurs of Oldmere
PUBLISHER: Editions Plavoc (AT THE BOTTOM OF THE COVER)
Updates

Target Market(s)

Readers of romantic novels

Industry/Entity Type

Book

```html
<!DOCTYPE html>
<html lang="en">
<head>
<meta charset="utf-8">
<title>The murmurs of Oldmere — Maribel Quonte</title>
<link href="https://fonts.googleapis.com/css2?family=Cinzel:wght@400&family=Lato:wght@300;400&display=swap" rel="stylesheet">
<style>
  :root {
    --backdrop: #f1f0ee;
    --sky-top: #7e2426;
    --sky-mid: #c93a2a;
    --sky-glow: #df5534;
    --dusk: #5a1713;
    --night: #140909;
    --ink-light: #ffffff;
  }
  html, body {
    margin: 0;
    padding: 0;
    width: 910px;
    height: 1200px;
    overflow: hidden;
    background: var(--backdrop);
  }
  .canvas {
    position: relative;
    width: 910px;
    height: 1200px;
  }
  .cover {
    position: absolute;
    left: 65px;
    top: 29px;
    width: 780px;
    height: 1142px;
    overflow: hidden;
    color: var(--ink-light);
  }
  .cover-photo {
    position: absolute;
    inset: 0;
    background:
      radial-gradient(ellipse 70% 30% at 55% 42%, rgba(230, 95, 60, 0.55), transparent 70%),
      linear-gradient(180deg,
        var(--sky-top) 0%,
        var(--sky-mid) 28%,
        var(--sky-glow) 45%,
        var(--sky-mid) 60%,
        var(--dusk) 76%,
        var(--night) 90%,
        var(--night) 100%);
  }
  .book-title { margin: 0; font-weight: 400; }
  .title-lead {
    position: absolute;
    left: 428px;
    top: 80px;
    margin: 0;
    font-family: "Lato", sans-serif;
    font-weight: 300;
    font-size: 82px;
    line-height: 72px;
    letter-spacing: -1px;
    white-space: nowrap;
  }
  .title-lead span { display: block; }
  .title-main {
    position: absolute;
    left: 0;
    right: 0;
    top: 302px;
    margin: 0;
    text-align: center;
    font-family: "Cinzel", serif;
    font-weight: 400;
    font-size: 134px;
    line-height: 1;
    letter-spacing: -2px;
    white-space: nowrap;
  }
  .title-main .initial { font-size: 156px; }
  .author {
    position: absolute;
    left: 428px;
    top: 472px;
    margin: 0;
    font-family: "Lato", sans-serif;
    font-weight: 300;
    font-size: 82px;
    line-height: 70px;
    letter-spacing: -1px;
    white-space: nowrap;
  }
  .author span { display: block; }
  .publisher {
    position: absolute;
    left: 0;
    right: 0;
    bottom: 54px;
    margin: 0;
    text-align: center;
    font-family: "Lato", sans-serif;
    font-weight: 400;
    font-size: 28px;
    letter-spacing: 0.3px;
  }
</style>
</head>
<body>
<main class="canvas">
  <section class="cover">
    <div class="cover-photo" role="img" aria-label="Photograph of a crimson sunset sky over the silhouetted domes of a lagoon city, with glowing street lanterns in the foreground"></div>
    <h1 class="book-title">
      <span class="title-lead"><span>the</span><span>murmurs</span><span>of</span></span>
      <span class="title-main"><span class="initial">O</span>LDMERE</span>
    </h1>
    <p class="author"><span>maribel</span><span>quonte</span></p>
    <p class="publisher">Éditions Plavoc</p>
  </section>
</main>
</body>
</html>
```